Business Card, Letterhead, Brochure, Gift Card, and Gift Card holder redesign

We are looking to refresh our print design work. (Business Card, Letterhead, Brochure, Gift Card, and Gift Card Holder) We do not need a logo redesign. We have recently redesigned our website and would like the print items to share its look. [url removed, login to view] I have attached sample of what our current print items look like as well as a vector format logo. We are very picky about quality and will most likely require a few revisions to get things right. We will expect to receive all source files and fonts used.

```html
<!DOCTYPE html>
<html lang="en">
<head>
<meta charset="utf-8">
<title>Lyra Spa &amp; Salon — Print Set</title>
<link href="https://fonts.googleapis.com/css2?family=Cormorant+Garamond:wght@400;500&family=Oswald:wght@400;500;600&display=swap" rel="stylesheet">
<style>
  :root{
    --page:#ececec;
    --navy:#1c2636;
    --navy-deep:#121a27;
    --sky:#a9bddf;
    --sky-light:#c3d2ea;
    --slate:#6e86ad;
    --bronze:#7a5330;
    --gold:#c89a5c;
    --ink:#1d2430;
    --paper:#ffffff;
    --label:#5a3a22;
  }
  *{box-sizing:border-box;margin:0;padding:0}
  html,body{width:1200px;height:749px;overflow:hidden}
  body{background:var(--page);position:relative;font-family:"Oswald",sans-serif;color:var(--ink)}

  .brand-name{font-family:"Cormorant Garamond",serif;font-weight:500;letter-spacing:.12em;line-height:1}
  .brand-tag{font-family:"Cormorant Garamond",serif;font-weight:400;letter-spacing:.04em;line-height:1}
  .mark{border-radius:50%;flex:none}

  /* Deliverables list */
  .deliverables{position:absolute;left:990px;top:24px;list-style:none;font-family:"Oswald",sans-serif;font-weight:500;font-size:17px;color:var(--label);line-height:1.45}

  /* Brochure spread */
  .brochure{position:absolute;left:34px;top:34px;width:450px;height:300px;display:flex;box-shadow:0 6px 18px rgba(0,0,0,.18)}
  .panel{flex:1;height:100%;padding:22px 16px;position:relative}
  .panel--info{background:var(--sky-light);border-right:1px solid rgba(0,0,0,.08)}
  .panel--info p{font-family:"Oswald",sans-serif;font-weight:400;font-size:11px;line-height:1.55;color:var(--navy)}
  .panel__photo{margin-top:18px;width:100%;height:120px;background:linear-gradient(135deg,#d7dde6,#8f9fb6)}
  .panel--cover{background:linear-gradient(160deg,var(--navy),var(--navy-deep));display:flex;flex-direction:column;align-items:center;justify-content:center;gap:10px}
  .panel--cover .mark{width:54px;height:54px;background:var(--gold)}
  .panel--cover .brand-name{font-size:30px;color:var(--slate)}
  .panel--cover .brand-tag{font-size:15px;color:var(--gold)}

  /* Business cards */
  .card{position:absolute;width:320px;height:184px;overflow:hidden;box-shadow:0 6px 16px rgba(0,0,0,.2)}
  .card--front{background:var(--sky)}
  .card__band{position:absolute;left:0;top:0;width:100%;height:100%}
  .card__brand{position:absolute;left:18px;top:16px;display:flex;align-items:center;gap:10px}
  .card__brand .mark{width:34px;height:34px;background:var(--gold)}
  .card__brand .brand-name{font-size:26px;color:var(--slate)}
  .card__tag{position:absolute;left:120px;top:44px;font-size:13px;color:var(--navy)}
  .card__person{position:absolute;left:116px;top:74px}
  .card__name{font-weight:600;font-size:14px;color:var(--navy);letter-spacing:.04em}
  .card__role{font-size:9px;color:var(--navy);letter-spacing:.06em;text-transform:uppercase}
  .card__contacts{position:absolute;left:116px;top:112px;list-style:none}
  .card__contacts li{display:flex;align-items:center;gap:8px;font-size:9.5px;font-weight:500;color:var(--navy);height:14px}
  .card__label{display:inline-block;width:30px;background:var(--bronze);color:#f3e6d6;font-size:8px;text-align:center;letter-spacing:.06em}
  .card__address{position:absolute;left:116px;top:160px;font-size:8.5px;line-height:1.25;color:var(--navy);text-transform:uppercase}
  .card--back{background:linear-gradient(180deg,var(--sky) 0%,var(--slate) 55%,var(--navy) 100%);display:flex;align-items:center;justify-content:center;gap:14px}
  .card--back .mark{width:48px;height:48px;background:var(--gold)}
  .card--back .brand-name{font-size:34px;color:var(--navy)}
  .card--back .brand-tag{font-size:14px;color:var(--navy);margin-top:6px}

  .set-a .card--back{left:560px;top:40px}
  .set-a .card--front{left:520px;top:132px}
  .set-b .card--back{left:800px;top:420px}
  .set-b .card--front{left:700px;top:520px}

  /* Letterhead */
  .letterhead{position:absolute;left:90px;top:372px;width:250px;height:354px;background:var(--paper);box-shadow:0 6px 18px rgba(0,0,0,.18)}
  .letterhead__brand{position:absolute;left:14px;top:14px;display:flex;align-items:center;gap:8px}
  .letterhead__brand .mark{width:26px;height:26px;background:var(--bronze)}
  .letterhead__brand .brand-name{font-size:20px;color:var(--slate)}
  .letterhead__tag{position:absolute;left:48px;top:38px;font-size:10px;color:var(--bronze)}
  .letterhead__footer{position:absolute;left:10px;right:10px;bottom:12px;border-top:2px solid var(--navy);padding-top:4px;display:flex;justify-content:space-between;font-size:7px;font-weight:500;color:var(--navy);letter-spacing:.03em}
</style>
</head>
<body>

<ul class="deliverables">
  <li>-BROCHURE</li>
  <li>-BUSSINESS CARD</li>
  <li>-HEADED PAPER</li>
</ul>

<section class="brochure" aria-label="Tri-fold brochure">
  <div class="panel panel--info">
    <p>Relax, restore and renew in our calm day spa.</p>
    <div class="panel__photo" role="img" aria-label="Photo of a spa treatment room"></div>
  </div>
  <div class="panel panel--info">
    <div class="panel__photo" role="img" aria-label="Photo of spa stones and towels" style="margin-top:0"></div>
    <p style="margin-top:14px">Massage, facials, nails and hair care by skilled hands.</p>
  </div>
  <div class="panel panel--cover">
    <span class="mark"></span>
    <span class="brand-name">LYRA</span>
    <span class="brand-tag">Spa &amp; Salon</span>
  </div>
</section>

<div class="set-a">
  <article class="card card--back" aria-label="Business card back">
    <span class="mark"></span>
    <div><div class="brand-name">LYRA</div><div class="brand-tag">Spa &amp; Salon</div></div>
  </article>
  <article class="card card--front" aria-label="Business card front">
    <svg class="card__band" viewBox="0 0 320 184" preserveAspectRatio="none" aria-hidden="true">
      <path d="M0 0 H92 Q70 92 92 184 H0 Z" fill="#1c2636"/>
    </svg>
    <div class="card__brand"><span class="mark"></span><span class="brand-name">LYRA</span></div>
    <div class="card__tag brand-tag">Spa &amp; Salon</div>
    <div class="card__person"><div class="card__name">NAME</div><div class="card__role">Position Title</div></div>
    <ul class="card__contacts">
      <li><span class="card__label">TEL</span>(555) 210-0148</li>
      <li><span class="card__label">EMAIL</span>INFO@LYRASPA.COM</li>
      <li><span class="card__label">WEB</span>WWW.LYRASPA.COM</li>
    </ul>
    <div class="card__address">1420 N. Willow Ave<br>Ashford, CA 90210</div>
  </article>
</div>

<section class="letterhead" aria-label="Letterhead">
  <div class="letterhead__brand"><span class="mark"></span><span class="brand-name">LYRA</span></div>
  <div class="letterhead__tag brand-tag">Spa &amp; Salon</div>
  <div class="letterhead__footer">
    <span>WWW.LYRASPA.COM</span><span>INFO@LYRASPA.COM</span><span>(555) 210-0148</span>
  </div>
</section>

<div class="set-b">
  <article class="card card--back" aria-label="Business card back, alternate">
    <span class="mark"></span>
    <div><div class="brand-name">LYRA</div><div class="brand-tag">Spa &amp; Salon</div></div>
  </article>
  <article class="card card--front" aria-label="Business card front, alternate">
    <svg class="card__band" viewBox="0 0 320 184" preserveAspectRatio="none" aria-hidden="true">
      <rect x="0" y="62" width="320" height="58" fill="#6e86ad" opacity=".55"/>
      <path d="M0 0 H92 Q70 92 92 184 H0 Z" fill="#3b4c66"/>
    </svg>
    <div class="card__brand"><span class="mark"></span><span class="brand-name">LYRA</span></div>
    <div class="card__tag brand-tag">Spa &amp; Salon</div>
    <div class="card__person"><div class="card__name">NAME</div><div class="card__role">Position Title</div></div>
    <ul class="card__contacts">
      <li><span class="card__label">TEL</span>555 318 2040</li>
      <li><span class="card__label">EMAIL</span>HELLO@LYRASPA.COM</li>
      <li><span class="card__label">WEB</span>WWW.LYRASPA.COM</li>
    </ul>
    <div class="card__address">2280 Harbor Ln<br>Ashford, CA 90211</div>
  </article>
</div>

</body>
</html>
```